Homepage design

Hi
I m workingon hosting my website tallowbrisk.net on wordpress but the new design for the homepage is not good
I need a design just for that page on how to organise things and what to put there

```html
<!DOCTYPE html>
<html lang="en">
<head>
<meta charset="utf-8">
<title>Tallow Brisk – Money Exchange &amp; Transfers</title>
<link href="https://fonts.googleapis.com/css2?family=PT+Sans:wght@400;700&family=Oswald:wght@500&display=swap" rel="stylesheet">
<style>
:root{
  --blue:#1f7fd0;
  --blue-light:#3fa3e6;
  --blue-dark:#1a6fc0;
  --navy:#0f2a55;
  --red:#c8201e;
  --ink:#2a2a2a;
  --muted:#6a6a6a;
  --line:#d9d9d9;
  --field:#f1f1f1;
  --footer:#f2f3f5;
  --bar:#e4e5e8;
}
*{margin:0;padding:0;box-sizing:border-box}
html,body{width:767px;height:1200px;overflow:hidden;background:#fff}
body{position:relative;font-family:"PT Sans",sans-serif;color:var(--ink)}
.abs{position:absolute}
a{color:inherit;text-decoration:none}

/* header */
.brand{left:62px;top:28px;display:flex;align-items:center;gap:8px;font-size:22px;font-weight:700;color:var(--blue-dark)}
.brand-dot{width:14px;height:14px;border-radius:50%;background:var(--red)}
.phone{left:506px;top:13px;font-size:13px;color:var(--blue);display:flex;align-items:center;gap:5px}
.lang{left:638px;top:10px;width:65px;height:20px;border:1px solid var(--line);font-size:8.5px;color:var(--muted);display:flex;align-items:center;gap:4px;padding-left:5px}
.lang-flag{width:14px;height:9px;background:#2a3f8a}
.nav{left:291px;top:43px;display:flex;align-items:center;font-size:11.5px;color:#333}
.nav a{padding:0 8px;border-left:1px solid #bbb;line-height:13px}
.nav a.home{background:var(--blue);color:#fff;border:0;line-height:23px;padding:0 13px;border-radius:2px}
.nav a.home + a{border-left:0}

/* hero */
.hero{left:0;top:84px;width:767px;height:280px;background:linear-gradient(100deg,#6d7e97 0%,#c9d2de 30%,#a9b3c0 55%,#d3d8df 80%,#8e99a8 100%)}
.hero-title{left:406px;top:256px;font-family:"Oswald",sans-serif;font-weight:500;font-size:27px;line-height:29px;color:#fff;letter-spacing:.3px;text-shadow:0 1px 3px rgba(0,0,0,.35)}
.dots{left:362px;top:346px;display:flex;gap:4px}
.dots span{width:9px;height:9px;border-radius:50%;background:rgba(255,255,255,.85)}

/* service band */
.band{left:0;top:364px;width:767px;height:152px;background:linear-gradient(#44a6e8,#1e79cf)}
.svc h3{font-size:14.5px;font-weight:400;color:#fff;margin-bottom:5px}
.svc p{font-size:8.5px;line-height:13.6px;color:#d8ecfb;width:190px}
.btn-outline{display:inline-block;margin-top:8px;border:1px solid rgba(255,255,255,.7);color:#fff;font-size:7.5px;padding:3px 10px;border-radius:2px}
.divider{top:384px;width:1px;height:110px;background:rgba(255,255,255,.25)}

/* main */
.intro{left:64px;top:548px;width:425px}
.intro h1{font-size:19px;font-weight:400;color:#222;margin-bottom:8px}
.intro .lead{font-size:10px;color:#333;margin-bottom:8px}
.intro p{font-size:8.2px;line-height:14px;color:var(--muted);margin-bottom:3px}
.news-head{left:66px;top:760px;font-size:18px;color:var(--blue)}
.news h4{font-size:9px;font-weight:700;color:#222;line-height:13.6px;width:200px}
.news p{font-size:8.2px;line-height:14px;color:var(--muted);margin-top:6px;width:200px}

.video{left:514px;top:552px;width:191px;height:134px;border:2px solid #e2e2e2;border-radius:3px;background:linear-gradient(135deg,#cfd6de,#8d98a6 70%,#b5a06a)}
.play{left:598px;top:606px;width:24px;height:24px;border-radius:50%;background:#111;border:2px solid #fff}

.quote{left:515px;top:696px;width:190px;height:230px;border:1px solid var(--line);border-radius:3px;overflow:hidden}
.quote-head{height:32px;background:var(--navy);color:#fff;font-size:13.5px;padding:7px 0 0 16px}
.field{position:absolute;left:14px;width:162px;height:18px;background:var(--field);border:1px solid #e1e1e1;font-size:7.5px;color:#555;padding:4px 0 0 9px}
.captcha-label{left:16px;top:148px;font-size:11px;color:#444}
.captcha{left:90px;top:146px;width:76px;height:16px;border:1px dashed #9aa;font-size:8px;font-style:italic;font-weight:700;color:#334;text-align:center;line-height:14px;letter-spacing:1px}
.btn-quote{left:107px;top:195px;width:69px;height:21px;background:var(--red);color:#fff;font-size:11px;font-weight:700;border-radius:2px;text-align:center;line-height:21px}

/* footer */
.footer{left:0;top:968px;width:767px;height:184px;background:var(--footer)}
.fcol h5{font-size:14px;font-weight:400;color:#333;margin-bottom:5px}
.fcol a{display:block;font-size:8.5px;line-height:15.2px;color:#444}
.badge{left:650px;top:1082px;width:38px;height:44px;border-radius:6px;background:linear-gradient(#e3c35a,#b08a2a)}
.bar{left:0;top:1152px;width:767px;height:48px;background:var(--bar)}
.copy{left:62px;top:1169px;font-size:8.5px;color:#555}
.social{left:577px;top:1166px;display:flex;gap:5px}
.social span{width:16px;height:16px;border-radius:2px}
</style>
</head>
<body>

<header>
  <div class="abs brand"><span class="brand-dot"></span>Tallow Brisk</div>
  <div class="abs phone">
    <svg width="14" height="14" viewBox="0 0 24 24"><path fill="#b5bcc4" d="M6.6 10.8a15 15 0 0 0 6.6 6.6l2.2-2.2c.3-.3.7-.4 1-.2 1.1.4 2.3.6 3.6.6.6 0 1 .4 1 1V20c0 .6-.4 1-1 1A17 17 0 0 1 3 4c0-.6.4-1 1-1h3.5c.6 0 1 .4 1 1 0 1.3.2 2.5.6 3.6.1.3 0 .7-.2 1z"/></svg>
    44 (0)20 7946 0381
  </div>
  <div class="abs lang"><span class="lang-flag"></span>English ▾</div>
  <nav class="abs nav">
    <a class="home" href="#">Home</a><a href="#">Personal</a><a href="#">Business</a><a href="#">Market Knowledge</a><a href="#">Currency tool</a><a href="#">Why Change</a>
  </nav>
</header>

<section>
  <div class="abs hero" role="img" aria-label="Photo of smiling business team giving thumbs up"></div>
  <div class="abs hero-title">WE PROVIDE BETTER<br>EXCHANGE RATES THAN BANKS</div>
  <div class="abs dots"><span></span><span></span><span></span><span></span></div>
</section>

<section>
  <div class="abs band"></div>
  <div class="abs divider" style="left:269px"></div>
  <div class="abs divider" style="left:492px"></div>
  <div class="abs svc" style="left:67px;top:386px">
    <h3>Personal Currency Exchange</h3>
    <p>Vivamus porttitor, g, purus nisi eleifend libero, a tempus libero lectus feugiat felis. Morbi diam mauris, viverra in, gravida eu, mattis in, ante. Morbi eget arcu. Morbi porta, libero</p>
    <a class="btn-outline" href="#">READ MORE</a>
  </div>
  <div class="abs svc" style="left:290px;top:386px">
    <h3>Business Currency Exchange</h3>
    <p>Vivamus porttitor, g, purus nisi eleifend libero, a tempus libero lectus feugiat felis. Morbi diam mauris, viverra in, gravida eu, mattis in, ante. Morbi eget arcu. Morbi porta, libero</p>
    <a class="btn-outline" href="#">READ MORE</a>
  </div>
  <div class="abs svc" style="left:515px;top:386px">
    <h3>Download Apps Now</h3>
  </div>
  <svg class="abs" style="left:518px;top:410px" width="34" height="54" viewBox="0 0 34 54"><rect x="2" y="2" width="30" height="50" rx="5" fill="none" stroke="#fff" stroke-width="2.5"/><line x1="2" y1="9" x2="32" y2="9" stroke="#fff" stroke-width="2"/><line x1="2" y1="44" x2="32" y2="44" stroke="#fff" stroke-width="2"/><line x1="13" y1="5.5" x2="21" y2="5.5" stroke="#fff" stroke-width="1.5"/></svg>
  <div class="abs svc" style="left:564px;top:410px">
    <p style="width:135px">Vivamus porttitor, g, purus nisi eleifend libero, a tempus libero lectus feugiat felis. Morbi diam mauris, viverra in, gravida</p>
  </div>
  <a class="abs btn-outline" href="#" style="left:567px;top:462px">DOWNLOAD</a>
</section>

<main>
  <div class="abs intro">
    <h1>Currency Exchange and International Payments</h1>
    <p class="lead">At Tallow Brisk we are a foreign currency broker for private and business clients.</p>
    <p>We place our business focus on providing our clients with the most competitive rates for currency exchange and money transfers whilst executing the highest quality of client service. Strategically located in London's financial district, we have immediate access to critical market insight enabling our clients to make a quick and informed decision as to when to convert currency.</p>
    <p>Our FX specialists buy and sell currency at rates close to interbank value. We monitor the currency market, work with live rates and aim to get the best rate at the time for our clients. Dealing with a large amount of international payments brings economies of scale which allows us to achieve even better exchange rates.</p>
    <p>As piece of mind for our clients is critical to our business, we operate to strict guidelines. Our principle bank is Harlow Mint in which our clients funds are held in secure segregated client accounts.</p>
  </div>

  <h2 class="abs news-head" style="font-weight:400">Latest News</h2>
  <article class="abs news" style="left:67px;top:790px">
    <h4>International Currency Exchange News 1st February to 8th February 2013:</h4>
    <p>Global markets report: Call us on +44 (0)20 7946 0381 or email us to info@tallowbrisk.net.</p>
  </article>
  <article class="abs news" style="left:291px;top:790px">
    <h4>Currency Exchange Report 8th February 2013:</h4>
    <p style="margin-top:10px">Global markets report: Call us on +44 (0)20 7946 0381 or email us to info@tallowbrisk.net...</p>
  </article>
  <article class="abs news" style="left:67px;top:866px">
    <h4>Foreign Exchange Report 7th February 2013:</h4>
    <p>Global markets report: Call us on +44 (0)20 7946 0381 or email us to info@tallowbrisk.net...</p>
  </article>
  <article class="abs news" style="left:291px;top:866px">
    <h4>Vivamus porttitor purus 10th February 2013:</h4>
    <p>In ullamcorper, est eget tempor cursus, neque mi consectetuer mi, a ultricies massa est sed nisl</p>
  </article>

  <div class="abs video" role="img" aria-label="Video still of a hand stacking coins"></div>
  <div class="abs play"></div>
  <svg class="abs" style="left:607px;top:613px" width="10" height="10" viewBox="0 0 10 10"><path d="M2 1l7 4-7 4z" fill="#fff"/></svg>

  <form class="abs quote">
    <div class="quote-head">Request Currency Quote</div>
    <div class="field" style="top:45px">Full Name</div>
    <div class="field" style="top:69px">Company name</div>
    <div class="field" style="top:94px">Phone no.</div>
    <div class="field" style="top:121px">Email address</div>
    <div class="abs captcha-label">Code Captcha</div>
    <div class="abs captcha">K7PLQX</div>
    <div class="field" style="top:170px">Image text</div>
    <div class="abs btn-quote">Get Quote</div>
  </form>
</main>

<footer>
  <div class="abs footer"></div>
  <div class="abs fcol" style="left:63px;top:997px">
    <h5>Services</h5>
    <a href="#">Open an individual account</a><a href="#">Open a business account</a><a href="#">Other services</a><a href="#">Refer a friend</a><a href="#">Affiliates</a>
  </div>
  <div class="abs fcol" style="left:183px;top:997px">
    <h5>Exchange</h5>
    <a href="#">Canadian dollars to US dollars</a><a href="#">Dollar to euros</a><a href="#">Dollar to pound</a><a href="#">Euros to dollars</a><a href="#">Euros to pounds</a>
  </div>
  <div class="abs fcol" style="left:314px;top:997px">
    <h5>Foreign Exchange</h5>
    <a href="#">Best euro rate</a><a href="#">Best exchange rates</a><a href="#">Currency exchange</a><a href="#">Currency news</a>
  </div>
  <div class="abs fcol" style="left:445px;top:999px">
    <h5>Currency Tools</h5>
    <a href="#">Calculator exchange rate</a><a href="#">Currency converter</a><a href="#">Currency conversion</a><a href="#">Foreign currency exchange rates</a>
  </div>
  <div class="abs fcol" style="left:590px;top:999px">
    <h5>Why Tallow Brisk</h5>
    <a href="#">About us</a><a href="#">Regulatory</a><a href="#">Careers</a><a href="#">Contact us</a>
  </div>
  <div class="abs badge" role="img" aria-label="Security badge"></div>

  <div class="abs bar"></div>
  <div class="abs copy">Copyright © Tallow Brisk 2012 Regulatory info | Disclaimer &amp; Privacy | Site Map | Sign In</div>
  <div class="abs social">
    <span style="background:#3b5a9a"></span><span style="background:#3a3a3a"></span><span style="background:#3aa0d8"></span><span style="background:#e8821e"></span><span style="background:#1d74b0"></span><span style="background:#c4302b"></span>
  </div>
</footer>

</body>
</html>
```